brightwave - Property Management DL Card

I am after a savvy designer to cut through junk mail! so many real estate agents use flyers to promote themselves and their business and usually sales. We are a property management firm (residential) and we want to represent landlords that have existing investment properties and need a quality agent to represent them. Can you help?
DL size, will be printed and delivered to mailboxes. For a look at our website go to www.brightwavehq.com.au. Keep it simple and clutter free.
it is to be double sided - with one side to be simple and clear - just our website, logo and telephone number on the back.
attached is our logo and our telephone number is 1300 42 18 96
the above are 2 essential elements to be included + our email address: admin@brightwavehq.com.au
also attached are our transparent price list

Target Market(s)
property investors,
people that manage properties themselves
Industry/Entity Type
Property Management
Other font styles liked:
- arial
Look and feel

```html
<!DOCTYPE html>
<html lang="en">
<head>
<meta charset="utf-8">
<title>brightwave – Property Management DL Card</title>
<link rel="stylesheet" href="https://fonts.googleapis.com/css2?family=Open+Sans:wght@300;400;600&display=swap">
<style>
  :root {
    --canvas: #d6d6d6;
    --ink-black: #050505;
    --panel-black: #0b0b0c;
    --sand: #e2d8b7;
    --brick: #c4402a;
    --brick-text: #d9402c;
    --soft-white: #f4f1ee;
    --muted-rose: #ecc9c0;
    --photo-light: #d9d3cc;
    --photo-dark: #6b5a48;
  }
  * { margin: 0; padding: 0; box-sizing: border-box; }
  html, body {
    width: 1200px; height: 1200px; overflow: hidden;
    background: var(--canvas);
    font-family: "Open Sans", Arial, sans-serif;
  }
  .card {
    position: absolute;
    left: 119px;
    width: 1002px;
    height: 500px;
    overflow: hidden;
    box-shadow: 0 2px 6px rgba(0,0,0,0.18);
  }
  .card--front { top: 56px; background: var(--panel-black); }
  .card--back { top: 637px; width: 1000px; background: var(--ink-black); }

  .front__band { position: absolute; left: 0; top: 0; width: 100%; height: 65px; background: var(--sand); }
  .front__photo {
    position: absolute; left: 0; top: 65px; width: 719px; height: 361px;
    background: linear-gradient(160deg, #ece8e3 0%, var(--photo-light) 45%, #a98f6f 78%, var(--photo-dark) 100%);
  }
  .front__brand-panel {
    position: absolute; left: 719px; top: 65px; width: 283px; height: 361px;
    background: var(--panel-black);
  }
  .brand-name {
    font-family: "Open Sans", Arial, sans-serif;
    font-weight: 300;
    color: var(--soft-white);
    letter-spacing: -0.5px;
    line-height: 1;
    white-space: nowrap;
  }
  .front__brand-panel .brand-name { position: absolute; left: 56px; top: 156px; font-size: 38px; }

  .front__strip {
    position: absolute; left: 0; top: 426px; width: 100%; height: 74px;
    background: var(--brick);
  }
  .strip__headline {
    position: absolute; left: 52px; top: 22px;
    font-size: 21px; font-weight: 400; color: var(--muted-rose);
  }
  .strip__divider {
    position: absolute; left: 423px; top: 17px; width: 1px; height: 38px;
    background: var(--muted-rose);
  }
  .strip__list {
    position: absolute; top: 16px; list-style: none;
    font-size: 16px; line-height: 21px; color: var(--soft-white);
  }
  .strip__list li::before { content: "•"; margin-right: 7px; }
  .strip__list--a { left: 448px; }
  .strip__list--b { left: 715px; }

  .card--back .brand-name { position: absolute; left: 54px; top: 46px; font-size: 44px; }
  .back__contact {
    position: absolute; left: 558px; top: 381px;
    padding-left: 21px; border-left: 1px solid #8c8c8c;
    font-size: 18px; line-height: 24px; letter-spacing: 0.3px;
    color: var(--soft-white); font-style: normal;
  }
  .back__phone { color: var(--brick-text); }
</style>
</head>
<body>
  <section class="card card--front">
    <div class="front__band"></div>
    <div class="front__photo" role="img" aria-label="Photograph of a modern open-plan apartment interior with staircase, dining table, pendant lights and timber kitchen"></div>
    <div class="front__brand-panel">
      <div class="brand-name">brightwave</div>
    </div>
    <div class="front__strip">
      <p class="strip__headline">Property Management specialists</p>
      <span class="strip__divider"></span>
      <ul class="strip__list strip__list--a">
        <li>Excellent communication</li>
        <li>Minimal vacancy</li>
      </ul>
      <ul class="strip__list strip__list--b">
        <li>No hidden extras</li>
        <li>The best rent return</li>
      </ul>
    </div>
  </section>

  <section class="card card--back">
    <div class="brand-name">brightwave</div>
    <address class="back__contact">
      <div class="back__phone">1300 42 18 96</div>
      <div>PO Box B527, Sydney South NSW, 1235</div>
      <div>admin@brightwavehq.com.au</div>
    </address>
  </section>
</body>
</html>
```